Harborline Restoration Business Card Design Phase 2

Professional and clean design. The design colors should flow with the logo. Two-sided card with the website on the back which is:

www.HarborlineRestoration.example.

"Specializing in Water Damage Restoration"

On the front I need the name, email, phone, and logo.

Name: Darnell Vickery
Email: Darnell@HarborlineRestoration.example
Phone: 555-018-2734 for now

I only have the Preview and Thumbnail right now but should have the source files uploaded within a day or two.

Target Market(s)

Flood victims, home owners with water damage from busted pipes etc...

Industry/Entity Type

Business

Contact Information for Business Card

Name: Darnell Vickery

Font styles to use
Serif
Sans Serif

Requirements
Must have
• Business Card Details Info

```html
<!DOCTYPE html>
<html lang="en">
<head>
<meta charset="utf-8">
<title>Harborline Restoration – Business Card</title>
<link rel="stylesheet" href="https://fonts.googleapis.com/css2?family=Open+Sans:wght@400;600;700&display=swap">
<style>
  :root {
    --navy: #1f3b6a;
    --green: #3f8b3a;
    --paper: #ffffff;
    --ink: #1e2f4f;
    --backdrop: #eceae6;
  }
  * { box-sizing: border-box; margin: 0; padding: 0; }
  html, body {
    width: 1200px;
    height: 900px;
    overflow: hidden;
    background: var(--backdrop);
    font-family: "Open Sans", Arial, sans-serif;
  }
  .canvas {
    position: relative;
    width: 1200px;
    height: 900px;
  }
  .card {
    position: absolute;
    width: 560px;
    height: 320px;
    border-radius: 3px;
    box-shadow: 0 6px 18px rgba(0,0,0,0.18);
    overflow: hidden;
  }
  /* Back side */
  .card-back {
    left: 90px;
    top: 110px;
    background: var(--navy);
    color: var(--paper);
  }
  .card-back .web-address {
    position: absolute;
    left: 190px;
    top: 40px;
    font-size: 13px;
    font-weight: 600;
    white-space: nowrap;
  }
  .card-back .tagline {
    position: absolute;
    left: 190px;
    top: 60px;
    font-size: 16px;
    font-weight: 700;
    white-space: nowrap;
  }
  .wordmark {
    position: absolute;
    display: flex;
    align-items: center;
    gap: 12px;
    font-weight: 700;
    font-size: 34px;
    line-height: 1.0;
    letter-spacing: 0.5px;
    text-transform: uppercase;
  }
  .wordmark .mark-square {
    width: 22px;
    height: 22px;
    flex: none;
  }
  .card-back .wordmark {
    left: 60px;
    bottom: 50px;
    color: var(--paper);
  }
  .card-back .wordmark .mark-square { background: var(--paper); }

  /* Front side */
  .card-front {
    left: 550px;
    top: 470px;
    background: var(--paper);
    color: var(--ink);
  }
  .card-front .holder-name {
    position: absolute;
    left: 250px;
    top: 34px;
    font-size: 17px;
    font-weight: 700;
    white-space: nowrap;
  }
  .holder-name .first { color: var(--green); }
  .holder-name .last { color: var(--navy); }
  .contact-list {
    position: absolute;
    left: 270px;
    top: 74px;
    list-style: none;
    font-size: 12.5px;
    color: var(--ink);
    white-space: nowrap;
  }
  .contact-list li {
    display: flex;
    align-items: center;
    gap: 9px;
    margin-bottom: 6px;
  }
  .contact-list svg { flex: none; }
  .card-front .wordmark {
    left: 50px;
    bottom: 60px;
    color: var(--navy);
  }
  .card-front .wordmark .mark-square { background: var(--green); }
</style>
</head>
<body>
<main class="canvas">

  <section class="card card-back" aria-label="Card back">
    <p class="web-address">www.HarborlineRestoration.example</p>
    <p class="tagline">Specializing in Water Damage Restoration</p>
    <div class="wordmark">
      <span class="mark-square"></span>
      <span class="wordmark-name">Harborline Restoration</span>
    </div>
  </section>

  <section class="card card-front" aria-label="Card front">
    <h1 class="holder-name"><span class="first">Darnell</span> <span class="last">Vickery</span></h1>
    <ul class="contact-list">
      <li class="contact-phone">
        <svg width="11" height="11" viewBox="0 0 24 24" aria-hidden="true">
          <path fill="#3f8b3a" d="M6.6 10.8a15.1 15.1 0 0 0 6.6 6.6l2.2-2.2a1 1 0 0 1 1-.25 11.4 11.4 0 0 0 3.6.57 1 1 0 0 1 1 1V20a1 1 0 0 1-1 1A17 17 0 0 1 3 4a1 1 0 0 1 1-1h3.5a1 1 0 0 1 1 1c0 1.25.2 2.45.57 3.6a1 1 0 0 1-.25 1z"/>
        </svg>
        <span>555-018-2734</span>
      </li>
      <li class="contact-email">
        <svg width="11" height="9" viewBox="0 0 24 18" aria-hidden="true">
          <rect width="24" height="18" rx="2" fill="#3f8b3a"/>
          <path d="M2 3l10 7 10-7" fill="none" stroke="#fff" stroke-width="2"/>
        </svg>
        <span>Darnell@HarborlineRestoration.example</span>
      </li>
    </ul>
    <div class="wordmark">
      <span class="mark-square"></span>
      <span class="wordmark-name">Harborline Restoration</span>
    </div>
  </section>

</main>
</body>
</html>
```